318 Diamond & Fastpitch Clinic 2017

Design a flyer that will promote our 2017 summer camp for boys and girls softball.

Weeks of
July 10th - 14th
July 17th - 21st.

Players ages 5 - 11.
Full day = 9:30am - 2:30pm half day = 9:30am - 11:30am.
$295 / full day : $195/ half day

Hosted by "318 Diamond" affiliated with the KV Meteors Touring Baseball & Softball Club and the Pine Hollow Junior League,

Camp Location PHJL, Lane 48C Maple Bluff.

PHone 555-284-7730, email info@318diamond.example

The color should be "Red white and blue color scheme" with dates and location standing out. 318 Logo should be prominent PHJL and Meteors smaller and secondary.

Feel free to use stock photo's if available. visit www.kvmeteors.example for more pictures and there are links for the 2017 summer camp there with possibly some more information.

Target Market(s)

to catch the eye of parents of players ages 5 - 11 already at little league or shopping in local stores

Colors
ec1f27
0355a3
ffffff

Requirements
Must have
• red white and blue design,
• 318 logo and summer camp prominent so it catches the eye and explains what it is right away.
• the meteors and pine hollow logo's a the bottom showing the affiliation.
Nice to have
• stock photo's or something showing players having a great time or a beautiful ballpark
Should not have
• to much clutter or hard to figure out what it's for

```html
<!DOCTYPE html>
<html lang="en">
<head>
<meta charset="utf-8">
<title>318 Diamond Softball Summer Camp 2017</title>
<link href="https://fonts.googleapis.com/css2?family=Oswald:wght@400;500;600;700&family=Yellowtail&display=block" rel="stylesheet">
<style>
  :root {
    --red: #c42027;
    --navy: #223a6b;
    --white: #ffffff;
    --ink: #1b1b1b;
    --grey-line: #6d6d6d;
    --orange: #d4502a;
    --backdrop: #6b7686;
    --photo-a: #8a8e55;
    --photo-b: #4f5a34;
  }
  html, body { margin: 0; padding: 0; width: 1200px; height: 1111px; overflow: hidden; background: var(--backdrop); }
  .canvas { position: relative; width: 1200px; height: 1111px; }
  .flyer { position: absolute; left: 230px; top: 12px; width: 740px; height: 1087px; box-shadow: 0 10px 30px rgba(0,0,0,.35); }
  .display { font-family: 'Oswald', sans-serif; font-weight: 700; }
  .label { font-family: 'Oswald', sans-serif; font-weight: 500; }
  .script { font-family: 'Yellowtail', cursive; }
</style>
</head>
<body>
<div class="canvas">
<svg class="flyer" viewBox="0 0 740 1087" xmlns="http://www.w3.org/2000/svg">
  <defs>
    <linearGradient id="photoTone" x1="0" y1="0" x2="1" y2="1">
      <stop offset="0" stop-color="var(--photo-a)"/>
      <stop offset="1" stop-color="var(--photo-b)"/>
    </linearGradient>
  </defs>

  <rect class="sheet" width="740" height="1087" fill="var(--white)"/>

  <rect class="hero-photo" role="img" aria-label="Young player in a red batting helmet and blue jersey on a grassy field" x="0" y="0" width="740" height="551" fill="url(#photoTone)"/>

  <polygon class="logo-panel" points="0,0 352,0 232,242 0,242" fill="var(--white)"/>
  <g class="brand-mark">
    <circle cx="66" cy="118" r="14" fill="var(--red)"/>
    <text class="display" x="92" y="145" font-size="78" fill="var(--red)">318</text>
  </g>

  <polygon class="date-band" points="0,380 410,380 320,698 0,698" fill="var(--red)"/>
  <polygon class="title-band" points="410,389 740,389 740,551 363,551" fill="var(--navy)"/>

  <text class="script" x="152" y="344" font-size="62" fill="var(--white)">softball</text>
  <text class="display" x="36" y="467" font-size="104" fill="var(--navy)" textLength="368" lengthAdjust="spacingAndGlyphs">SUMMER</text>
  <text class="display" x="404" y="467" font-size="104" fill="var(--white)" textLength="226" lengthAdjust="spacingAndGlyphs">CAMP</text>
  <text class="display" transform="translate(645,380) rotate(90)" font-size="40" fill="var(--white)" textLength="88" lengthAdjust="spacingAndGlyphs">2017</text>
  <text class="script" x="446" y="493" font-size="24" fill="var(--white)">for boys and girls</text>
  <line class="divider" x1="42" y1="515" x2="614" y2="515" stroke="var(--white)" stroke-width="2" stroke-dasharray="9 7"/>

  <g class="dates label" fill="var(--white)" font-size="32">
    <text x="68" y="593">WEEKS OF</text>
    <text x="68" y="639">JULY 10TH - 14TH</text>
    <text x="68" y="686">JULY 17TH - 21ST.</text>
  </g>

  <g class="players-icon" fill="var(--navy)">
    <circle cx="411" cy="568" r="5"/>
    <rect x="405" y="575" width="12" height="14" rx="2"/>
    <rect x="406" y="588" width="4" height="12"/>
    <rect x="412" y="588" width="4" height="12"/>
    <circle cx="428" cy="568" r="5"/>
    <polygon points="428,574 420,592 436,592"/>
    <rect x="423" y="591" width="4" height="9"/>
    <rect x="429" y="591" width="4" height="9"/>
  </g>
  <g class="label" fill="var(--navy)" font-size="29">
    <text x="451" y="597">PLAYERS</text>
    <text x="451" y="642">AGES</text>
  </g>
  <circle class="age-badge" cx="630" cy="621" r="61" fill="var(--navy)"/>
  <text class="label" x="630" y="633" font-size="34" fill="var(--white)" text-anchor="middle">5 - 11</text>

  <g class="clock-icon" fill="none" stroke="var(--red)" stroke-width="3">
    <circle cx="74" cy="784" r="12"/>
    <line x1="74" y1="784" x2="74" y2="776"/>
    <line x1="74" y1="784" x2="80" y2="788"/>
    <line x1="70" y1="768" x2="78" y2="768"/>
  </g>
  <g class="label" fill="var(--red)" font-size="21">
    <text x="104" y="781">FULL DAY = 9:30AM - 2:30PM</text>
    <text x="104" y="811">HALF DAY = 9:30AM - 11:30AM.</text>
  </g>

  <text class="script" x="448" y="793" font-size="22" fill="var(--navy)" text-anchor="end">Cost:</text>
  <circle cx="471" cy="786" r="15" fill="var(--navy)"/>
  <text class="label" x="471" y="794" font-size="20" fill="var(--white)" text-anchor="middle">$</text>
  <g class="label" fill="var(--navy)" font-size="21">
    <text x="497" y="781">$295 / FULL DAY</text>
    <text x="497" y="811">$195/ HALF DAY</text>
  </g>

  <line class="divider" x1="26" y1="835" x2="703" y2="835" stroke="var(--grey-line)" stroke-width="1.5" stroke-dasharray="7 6"/>

  <g class="label" fill="var(--ink)" font-size="11">
    <text x="39" y="878">HOSTED BY "318 DIAMOND"</text>
    <text x="39" y="895">AFFILIATED WITH THE KV METEORS TOURING BASEBALL &amp; SOFTBALL CLUB AND</text>
    <text x="39" y="912">THE PINE HOLLOW JUNIOR LEAGUE</text>
  </g>
  <text class="display" x="525" y="904" font-size="30" fill="var(--red)" text-anchor="middle">METEORS</text>
  <g class="partner-mark">
    <circle cx="618" cy="895" r="6" fill="var(--navy)"/>
    <text class="label" x="629" y="901" font-size="15" fill="var(--navy)">PINE HOLLOW</text>
  </g>

  <line x1="26" y1="942" x2="703" y2="942" stroke="var(--ink)" stroke-width="1.5"/>
  <line x1="26" y1="952" x2="703" y2="952" stroke="var(--grey-line)" stroke-width="1.5" stroke-dasharray="7 6"/>

  <g class="script" fill="var(--orange)" font-size="40">
    <text transform="translate(56,1010) rotate(-8)">Register</text>
    <text transform="translate(64,1058) rotate(-8)">today!</text>
  </g>

  <path class="pin-icon" d="M241 984 a8 8 0 0 1 8 8 c0 6 -8 15 -8 15 s-8 -9 -8 -15 a8 8 0 0 1 8 -8z" fill="var(--navy)"/>
  <circle cx="241" cy="992" r="3" fill="var(--white)"/>
  <text class="script" x="262" y="1003" font-size="22" fill="var(--navy)">Camp Location:</text>
  <g class="label" fill="var(--ink)" font-size="18">
    <text x="262" y="1034">CAMP LOCATION PHJL,</text>
    <text x="262" y="1060">LANE 48C MAPLE BLUFF.</text>
  </g>

  <g class="phone-icon" fill="var(--navy)">
    <rect x="468" y="985" width="13" height="22" rx="2"/>
    <rect x="471" y="989" width="7" height="10" fill="var(--white)"/>
    <rect x="472" y="979" width="2" height="7"/>
  </g>
  <text class="script" x="489" y="1003" font-size="22" fill="var(--navy)">Contact:</text>
  <g class="label" fill="var(--ink)" font-size="18">
    <text x="489" y="1034">PHONE 555-284-7730, EMAIL</text>
    <text x="489" y="1060">INFO@318DIAMOND.EXAMPLE</text>
  </g>
</svg>
</div>
</body>
</html>
```